Travel Agency Website - Simple General

Need a 7 page simple design that is pretty repetitive. Need to be able to load quickly that is SEO optimized. Trying to give ideas on what they can do, be personal as we are local, but at the same time come across as professional and get information easily with little burden.

- Landing Page
- Brambleton Vacations Page
- Family Trips
- Road Trips from Texas
- Other Destinations
- About Us Page
- Contact Us Page

Target Market(s)

Families

Coding

Coded - Design and coding required

Number of Pages Required

5+ page

Colors

Designer to choose colors to be used in the design.

Requirements
Must have
• Like it to flow easily with our logo. Use that for colors, etc.

```html
<!DOCTYPE html>
<html lang="en">
<head>
<meta charset="utf-8">
<title>Hum Along As You Roam Travel Co.</title>
<link href="https://fonts.googleapis.com/css2?family=Amaranth:wght@400;700&family=Fira+Sans+Condensed:wght@400;600&family=Lilita+One&family=Fira+Sans+Extra+Condensed:wght@600&display=swap" rel="stylesheet">
<style>
  :root{
    --navy:#06172a;
    --teal:#4e9aa0;
    --teal-deep:#17505d;
    --teal-light:#8cc4c5;
    --gold:#c49a4e;
    --nav-blue:#1d4779;
    --pale:#dcdde3;
    --white:#ffffff;
    --orange-a:#ff5f5b;
    --orange-b:#ff8e1f;
  }
  *{box-sizing:border-box;margin:0;padding:0}
  html,body{width:1200px;height:1169px;overflow:hidden;background:var(--navy)}
  .page{position:relative;width:1200px;height:1169px;overflow:hidden;font-family:"Fira Sans Condensed",sans-serif;color:var(--white)}
  .backdrop{position:absolute;inset:0}
  .topbar{position:absolute;top:0;left:0;width:1200px;height:90px}
  .contact-item{position:absolute;top:20px;display:flex;align-items:center;gap:14px;font-weight:600;font-size:20px}
  .contact-item.email{left:108px}
  .contact-item.phone{left:915px}
  .diamond{width:32px;height:32px;display:flex;align-items:center;justify-content:center}
  .brand-mark{position:absolute;left:545px;top:18px;width:110px;text-align:center;font-family:"Amaranth",sans-serif;font-weight:700;font-size:15px;line-height:1.15;color:var(--white)}
  .main-nav{position:absolute;top:96px;left:0;width:1200px;display:flex;justify-content:center;gap:7px}
  .main-nav a{display:block;height:40px;line-height:38px;padding:0 14px;border:1px solid rgba(255,255,255,.45);border-radius:4px;background:var(--nav-blue);color:var(--white);text-decoration:none;text-transform:uppercase;font-family:"Fira Sans Extra Condensed",sans-serif;font-weight:600;font-size:16px}
  .main-nav a.active{background:var(--gold);padding:0 20px}
  .hero-text{position:absolute;top:172px;left:0;width:1200px;text-align:center}
  .welcome{font-family:"Amaranth",sans-serif;font-weight:700;font-size:27px;margin-left:-20px;text-shadow:0 2px 4px rgba(0,0,0,.4)}
  .hero-title{font-family:"Lilita One",sans-serif;font-weight:400;font-size:84px;line-height:74px;text-align:left;width:560px;margin:4px 0 0 345px;text-shadow:0 3px 6px rgba(0,0,0,.45)}
  .hero-lead{font-size:18px;line-height:26px;margin-top:8px;text-shadow:0 1px 3px rgba(0,0,0,.6)}
  .cta{position:absolute;left:494px;top:426px;width:213px;height:68px;border:2px solid var(--white);border-radius:4px;padding:5px}
  .cta a{display:block;height:100%;border-radius:3px;background:linear-gradient(90deg,var(--orange-a),var(--orange-b));color:var(--white);text-decoration:none;text-align:center;line-height:54px;font-family:"Amaranth",sans-serif;font-weight:700;font-size:24px}
  .trip{position:absolute;width:256px;height:256px;border-radius:50%;border:5px solid var(--white);display:flex;align-items:center;justify-content:center;text-align:center;overflow:hidden}
  .trip .photo{position:absolute;inset:0}
  .trip span{position:relative;font-family:"Amaranth",sans-serif;font-weight:700;font-size:31px;line-height:34px;text-shadow:0 2px 5px rgba(0,0,0,.6)}
  .footer{position:absolute;top:870px;left:0;width:1200px}
  .footer-brand{position:absolute;left:108px;top:40px;width:160px;text-align:center;font-family:"Amaranth",sans-serif;font-weight:700;font-size:22px;line-height:1.15}
  .footer-col{position:absolute;top:10px}
  .footer-col h3{font-family:"Amaranth",sans-serif;font-weight:700;font-size:20px;margin-bottom:16px}
  .footer-col ul{list-style:none}
  .footer-col li{display:flex;align-items:center;gap:8px;font-size:17px;height:37px}
  .footer-col.social li{height:43px;gap:10px}
  .icon-dot{width:22px;height:22px;border-radius:50%;background:var(--gold)}
  .col-links{left:410px}
  .col-travel{left:664px}
  .col-social{left:954px}
  .copyright{position:absolute;left:0;top:1133px;width:1200px;height:36px;background:var(--teal-deep);text-align:center;line-height:36px;font-size:15px}
  .copyright em{font-style:normal;color:var(--teal-light)}
</style>
</head>
<body>
<div class="page">
  <svg class="backdrop" width="1200" height="1169" viewBox="0 0 1200 1169" aria-hidden="true">
    <defs>
      <linearGradient id="canyon" x1="0" y1="0" x2="0" y2="1">
        <stop offset="0" stop-color="#1b3f66"/>
        <stop offset=".35" stop-color="#6e4a4a"/>
        <stop offset=".7" stop-color="#7a4d39"/>
        <stop offset="1" stop-color="#4f3a2d"/>
      </linearGradient>
    </defs>
    <rect width="1200" height="1169" fill="var(--navy)"/>
    <rect width="1200" height="870" fill="var(--pale)"/>
    <polygon points="0,0 1200,0 1200,339 600,590 0,339" fill="url(#canyon)"/>
    <polyline points="0,345 600,596 1200,345" fill="none" stroke="var(--teal)" stroke-width="12"/>
    <polygon points="0,862 600,590 1200,862 1200,1169 0,1169" fill="var(--navy)"/>
  </svg>
  <div role="img" aria-label="Canyon trail with riders on horseback beneath red rock spires" style="position:absolute;left:0;top:0;width:1200px;height:590px"></div>

  <header class="topbar">
    <div class="contact-item email">
      <span class="diamond"><svg width="32" height="32" viewBox="0 0 32 32"><rect x="6" y="6" width="20" height="20" transform="rotate(45 16 16)" fill="var(--teal)"/><rect x="10" y="11" width="12" height="9" rx="1" fill="#fff"/><polyline points="10,11 16,16 22,11" fill="none" stroke="var(--teal)" stroke-width="1.5"/></svg></span>
      hello@humalongroam.net
    </div>
    <div class="brand-mark">Hum Along As You Roam</div>
    <div class="contact-item phone">
      <span class="diamond"><svg width="32" height="32" viewBox="0 0 32 32"><rect x="6" y="6" width="20" height="20" transform="rotate(45 16 16)" fill="var(--teal)"/><path d="M12 10c1 0 2 2.5 2 3s-1 1-1 1.5c.5 1.5 2 3 3.5 3.5.5 0 1-1 1.5-1s3 1 3 2-1.5 2-2.5 2c-4 0-8.5-4.5-8.5-8.5 0-1 1-2.5 2-2.5z" fill="#fff"/></svg></span>
      111.111.1111
    </div>
  </header>

  <nav class="main-nav">
    <a class="active" href="#">Home</a>
    <a href="#">Brambleton Vacations</a>
    <a href="#">Family Trips</a>
    <a href="#">Texas Road Trips</a>
    <a href="#">Other Destinations</a>
    <a href="#">About Us</a>
    <a href="#">Contact Us</a>
  </nav>

  <section class="hero-text">
    <p class="welcome">Welcome to</p>
    <h1 class="hero-title">Hum Along As<br>You Roam</h1>
    <p class="hero-lead">It was popularised in the 1960s with the release of Letterfold sheets<br>containing Lorem Ipsum passages,</p>
  </section>
  <div class="cta"><a href="#">Contact Us</a></div>

  <a class="trip" style="left:103px;top:537px">
    <div class="photo" role="img" aria-label="Fairytale castle with blue spires" style="background:linear-gradient(180deg,#3c6a96,#2c4d72 60%,#1f3556)"></div>
    <span>Brambleton<br>Vacations</span>
  </a>
  <a class="trip" style="left:349px;top:545px">
    <div class="photo" role="img" aria-label="Family taking a selfie by a bridge" style="background:linear-gradient(180deg,#4d7595,#3a5269 55%,#2b3a45)"></div>
    <span>Family<br>Trips</span>
  </a>
  <a class="trip" style="left:593px;top:553px">
    <div class="photo" role="img" aria-label="Friends posing beside a red car" style="background:linear-gradient(180deg,#5b6e82,#5a4e55 55%,#3b4d66)"></div>
    <span>Texas Road<br>Trips</span>
  </a>
  <a class="trip" style="left:838px;top:560px">
    <div class="photo" role="img" aria-label="Airplane parked on an airport apron" style="background:linear-gradient(180deg,#5f8a9c,#4a6d7d 55%,#3d5360)"></div>
    <span>Other<br>Destinations</span>
  </a>

  <footer class="footer">
    <div class="footer-brand">Hum Along As You Roam</div>
    <div class="footer-col col-links">
      <h3>Quick Link</h3>
      <ul>
        <li><svg width="18" height="18" viewBox="0 0 18 18"><path d="M9 0L10.5 7.5 18 9 10.5 10.5 9 18 7.5 10.5 0 9 7.5 7.5z" fill="var(--gold)"/></svg>Home</li>
        <li><svg width="18" height="18" viewBox="0 0 18 18"><path d="M9 0L10.5 7.5 18 9 10.5 10.5 9 18 7.5 10.5 0 9 7.5 7.5z" fill="var(--gold)"/></svg>About Us</li>
        <li><svg width="18" height="18" viewBox="0 0 18 18"><path d="M9 0L10.5 7.5 18 9 10.5 10.5 9 18 7.5 10.5 0 9 7.5 7.5z" fill="var(--gold)"/></svg>Contact Us</li>
      </ul>
    </div>
    <div class="footer-col col-travel">
      <h3>Travel</h3>
      <ul>
        <li><svg width="18" height="18" viewBox="0 0 18 18"><path d="M9 0L10.5 7.5 18 9 10.5 10.5 9 18 7.5 10.5 0 9 7.5 7.5z" fill="var(--gold)"/></svg>Brambleton Vacations</li>
        <li><svg width="18" height="18" viewBox="0 0 18 18"><path d="M9 0L10.5 7.5 18 9 10.5 10.5 9 18 7.5 10.5 0 9 7.5 7.5z" fill="var(--gold)"/></svg>Family Trips</li>
        <li><svg width="18" height="18" viewBox="0 0 18 18"><path d="M9 0L10.5 7.5 18 9 10.5 10.5 9 18 7.5 10.5 0 9 7.5 7.5z" fill="var(--gold)"/></svg>Texas Road Trips</li>
        <li><svg width="18" height="18" viewBox="0 0 18 18"><path d="M9 0L10.5 7.5 18 9 10.5 10.5 9 18 7.5 10.5 0 9 7.5 7.5z" fill="var(--gold)"/></svg>Other Destinations</li>
      </ul>
    </div>
    <div class="footer-col col-social social">
      <h3>Get Social</h3>
      <ul>
        <li><span class="icon-dot"></span>Friendpage</li>
        <li><span class="icon-dot"></span>Snapgram</li>
      </ul>
    </div>
  </footer>

  <div class="copyright">© 2026 <em>HUM ALONG AS YOU ROAM</em>. All right reserved.</div>
</div>
</body>
</html>
```